Presentation Folder, Business Card, Letterhead and Envelope design

We are a dental clinic that will open in August and we are looking for a professional graphic designer to create our Business Card, Presentation Folder, Letterhead, Notepad and envelopes.

The brand NovaGrin must reflect a sense of quality and sophistication, marketed for middle-class consumers.
Our preference is for quality and refined materials, where less is more.
Attached the logo

```html
<!DOCTYPE html>
<html lang="en">
<head>
<meta charset="utf-8">
<title>NovaGrin Envelope Set</title>
<link href="https://fonts.googleapis.com/css2?family=Jost:wght@300;400&display=swap" rel="stylesheet">
<style>
  :root {
    --slate: #585958;
    --burgundy: #6a1212;
    --paper: #ffffff;
    --edge: #c9c9c9;
    --ink-light: #ffffff;
  }
  html, body {
    margin: 0;
    padding: 0;
    width: 1200px;
    height: 997px;
    overflow: hidden;
    background: var(--paper);
  }
  .stationery {
    display: block;
    width: 1200px;
    height: 997px;
    font-family: "Jost", sans-serif;
  }
  .envelope-edge { fill: none; stroke: var(--edge); stroke-width: 1; }
  .fill-slate { fill: var(--slate); }
  .fill-burgundy { fill: var(--burgundy); }
  .fill-paper { fill: var(--paper); }
  .flap-text { fill: var(--ink-light); font-size: 7.6px; font-weight: 400; }
  .brand-name {
    fill: var(--slate);
    font-size: 22px;
    font-weight: 300;
    letter-spacing: 6.5px;
  }
  .contact-text { fill: var(--slate); font-size: 7.2px; font-weight: 400; }
  .contact-icon { fill: var(--slate); }
  .contact-line { fill: none; stroke: var(--slate); stroke-width: 0.8; }
</style>
</head>
<body>
<svg class="stationery" viewBox="0 0 1200 997" xmlns="http://www.w3.org/2000/svg">

  <!-- Back of envelope -->
  <g class="envelope-back">
    <polygon class="fill-slate" points="91,77 563,77 585,183 69,183"/>
    <rect class="fill-paper" x="69" y="183" width="516" height="731"/>
    <rect class="fill-slate" x="69" y="183" width="516" height="560"/>
    <line x1="69" y1="183" x2="585" y2="183" stroke="#4a4b4a" stroke-width="0.8"/>
    <rect class="envelope-edge" x="69" y="183" width="516" height="731"/>

    <g class="flap-address" transform="rotate(180 460 150)">
      <text class="flap-text" x="387" y="147">www.novagrin-dental.com</text>
      <text class="flap-text" x="387" y="157">Elm Lane 4-7B, Bristol</text>
    </g>

    <g class="brand">
      <rect class="fill-burgundy" x="104" y="782" width="22" height="22"/>
      <text class="brand-name" x="133" y="802">NOVAGRIN</text>
    </g>
  </g>

  <!-- Front of envelope -->
  <g class="envelope-front">
    <rect class="fill-paper" x="614" y="183" width="516" height="731"/>
    <polygon class="fill-slate" points="614,183 1130,183 1108,288 637,288"/>
    <rect class="envelope-edge" x="614" y="183" width="516" height="731"/>

    <g class="flap-address">
      <text class="flap-text" x="665" y="213">www.novagrin-dental.com</text>
      <text class="flap-text" x="665" y="223">Elm Lane 4-7B, Bristol</text>
    </g>

    <g class="brand">
      <rect class="fill-burgundy" x="652" y="856" width="22" height="22"/>
      <text class="brand-name" x="681" y="876">NOVAGRIN</text>
    </g>

    <g class="contact-list">
      <path class="contact-icon" d="M1000 845.5 l1.8 0 l0.9 1.8 l-0.9 0.9 q0.9 1.8 2.7 2.7 l0.9 -0.9 l1.8 0.9 l0 1.8 q-5.4 0 -7.2 -7.2 Z"/>
      <text class="contact-text" x="1009" y="851">+00 987 654 321</text>

      <rect class="contact-line" x="1000" y="856.5" width="5.5" height="4"/>
      <path class="contact-line" d="M1000 856.5 l2.75 2.2 l2.75 -2.2"/>
      <text class="contact-text" x="1009" y="861">hello@novagrin.com</text>

      <circle class="contact-line" cx="1002.8" cy="868.6" r="2.6"/>
      <path class="contact-line" d="M1000.2 868.6 h5.2 M1002.8 866 v5.2"/>
      <text class="contact-text" x="1009" y="871">www.novagrin-dental.com</text>

      <path class="contact-icon" d="M1002.8 882.5 l-2.3 -3.6 a2.6 2.6 0 1 1 4.6 0 Z"/>
      <circle cx="1002.8" cy="877.6" r="0.9" fill="var(--paper)"/>
      <text class="contact-text" x="1009" y="881">Elm Lane 4-7B, Bristol</text>
    </g>
  </g>
</svg>
</body>
</html>
```